K M Guard Solutions - Alarm and CCTV installation Flyer

Need a flyer designed that grabs the attention of potential customers, we need the price to stand out the most to grab people’s attention, whether they are residential or commercial.We are a security company based in Brentwood Essex but cover London and the home counties. here is our website to take a look at www.kmguardsolutions.co.uk. We want them to know we install complete alarm and Cctv systems and will keep them “safe”

Target Market(s)

residential and commercial property

Colors
f37122

Requirements
Must have
• on one side
• large clear logo - professional design
• - Intruder Alarms starting from £495 + VAT. (Big text)
• - £150 discount on installations
• *terms and conditions apply (small text)
• - Not happy with your current provider? Free of charge no obligation take over survey and quotation and up to £100 off
• - CCTV systems starting from £595 + VAT (based on 2 cameras)
• K M Guard Solutions are always there, always available, wherever and whenever you need us.
• Large telephone number at the bottom 01632 480913
• Address / email / website as a footer * see website for details
• on second side
• large and bold
• Are you looking to keep you and your premises safe?
• - K M Guard Solutions install, maintain and repair all intruder alarms, CCTV, intercom and access control
• - View, control and manage your security systems anywhere in the world
• - Feel at ease with monitoring services & police response tailored to suit you and your business
• - K M Guard can takeover any existing security system and offer maintenance checks to guarantee the best performance for you and your premises
• - K M Guard understand that being security conscious is ever increasing, protecting your property and family is a number one priority
• - Our fully insured and accredited team offer quality, safety and cost efficiency throughout the whole process
• - K M Guard Solutions are using the latest cloud-based technology to stay connected with your home and business 24/7
• If you are looking to improve the security in your home, office or commercial property then call a member of our team today for a free quote.
• Fully insured and accredited
• Tradevouch logo and NQPB Intruder and CCTV logos
• Logo somewhere on page and
• Telephone number
• Address / email / website as footer
Nice to have
• We would like to have the text saying
• Intruder alarms installed from £495 + vat the biggest text on the page. Most likely the £495 part the largest.
• Also would like “not happy with your current provider” more obvious
• We would like use our company colours - Orange/White/black

```html
<!DOCTYPE html>
<html lang="en">
<head>
<meta charset="utf-8">
<title>K M Guard Solutions – Alarm and CCTV Flyer</title>
<link rel="stylesheet" href="https://fonts.googleapis.com/css2?family=Oswald:wght@500;600&family=Source+Sans+3:wght@300;400;600;700&display=swap">
<style>
:root{
  --orange:#ee5124;
  --black:#0b0b0b;
  --cream:#efebe2;
  --ink:#3a3a3a;
  --backdrop:#3c3c3e;
  --white:#ffffff;
}
*{box-sizing:border-box;margin:0;padding:0}
html,body{width:1200px;height:866px;overflow:hidden;background:var(--backdrop)}
body{position:relative;font-family:"Source Sans 3",sans-serif;color:var(--ink)}
.flyer{position:absolute;top:78px;width:496px;height:695px;background:var(--cream);overflow:hidden;box-shadow:4px 6px 14px rgba(0,0,0,.45)}
.flyer--front{left:80px}
.flyer--back{left:612px;width:494px}
.abs{position:absolute}
.header{left:0;top:0;width:100%;height:104px;background:var(--orange);color:var(--white)}
.front-title{left:26px;top:14px;font-weight:700;font-size:39px;line-height:1;letter-spacing:.2px}
.front-price{left:26px;top:56px;font-weight:600;font-size:32px;line-height:1.1}
.front-price b{font-weight:700}
.photo{background:linear-gradient(135deg,#d9dde0,#eef0ef 45%,#b9a998 80%,#8f877d)}
.band{background:var(--black);color:var(--white)}
.cond{font-family:"Oswald",sans-serif;font-weight:600}
.discount{left:26px;top:302px;font-size:21px;letter-spacing:.2px}
.terms{left:26px;top:334px;font-size:7px;color:#ddd;letter-spacing:.3px}
.phones{left:306px;top:306px;width:168px;height:178px;border-radius:14px;background:linear-gradient(160deg,#1c1c1e,#3a7fc2 40%,#f4f5f7 60%,#c9ccd1)}
.provider{left:26px;top:360px;font-weight:700;font-size:18px;line-height:1.2;color:#333}
.survey{left:26px;top:406px;font-size:12px;line-height:1.35;width:260px}
.survey .hl{color:var(--orange);font-weight:700}
.survey b{font-weight:700}
.point{font-size:11px;line-height:1.45;color:#333}
.point::before{content:"";position:absolute;left:-28px;top:3px;width:20px;height:20px;border-radius:50%;background:var(--orange)}
.brand{left:26px;top:600px;display:flex;align-items:center;gap:10px}
.brand .mark{width:26px;height:26px;background:var(--orange)}
.brand .name{font-weight:700;font-size:20px;color:var(--orange);line-height:1.05}
.contact-label{right:30px;top:508px;font-weight:300;font-size:22px;color:#444}
.phone-big{right:30px;top:535px;font-size:34px;color:#333;letter-spacing:1px;line-height:1.2}
.web{right:30px;top:585px;font-size:14px;font-weight:600;color:var(--orange)}
.email{right:30px;top:611px;font-size:12px;color:#333}
.address{right:30px;top:634px;font-size:12px;color:#333;text-align:right;line-height:1.45}
.footer{left:0;bottom:0;width:100%;height:19px}
.back-title{left:0;top:16px;width:100%;text-align:center;font-weight:700;font-size:32px;line-height:1.25}
.view{left:22px;top:306px;font-size:15.5px;line-height:1.2;letter-spacing:.2px}
.view .o{color:var(--orange)}
.back-point{left:51px;width:225px}
.cta{left:326px;top:291px;width:164px;height:187px;background:var(--orange);color:var(--white);text-align:center}
.cta p{padding:14px 8px 0;font-weight:700;font-size:11.5px;line-height:1.4}
.cta h3{margin-top:14px;font-family:"Oswald",sans-serif;font-weight:600;font-size:19.5px;line-height:1.1;color:var(--black)}
.listing{left:342px;top:491px;width:112px;height:35px;background:var(--white);border-radius:2px}
.listing span{position:absolute;left:10px;top:10px;width:92px;height:14px;border-radius:3px;background:linear-gradient(90deg,#d9442b,#1d6fb5)}
.cert{top:535px;width:49px;height:66px;background:var(--white);border:1px solid #cfcfcf}
.cert i{position:absolute;left:8px;top:6px;width:32px;height:32px;border-radius:50%;border:3px solid #1f3b73}
.cert em{position:absolute;left:10px;top:46px;width:28px;height:4px;background:#1f3b73}
.back-phone{right:18px;top:616px;font-size:32px;color:var(--orange);letter-spacing:.5px;line-height:1.2}
.back-web{right:20px;top:656px;font-size:11.5px;font-weight:700;color:#333;letter-spacing:.8px}
</style>
</head>
<body>

<section class="flyer flyer--front">
  <div class="abs header">
    <h1 class="abs front-title">INTRUDER ALARMS</h1>
    <p class="abs front-price">Starting from <b>£495 + VAT</b></p>
  </div>
  <div class="abs photo" style="left:0;top:104px;width:100%;height:195px" role="img" aria-label="Photo of a modern kitchen with a wall-mounted touchscreen alarm panel"></div>

  <svg class="abs" style="left:0;top:299px" width="496" height="60" viewBox="0 0 496 60" aria-hidden="true">
    <rect width="496" height="60" fill="var(--black)"/>
    <path d="M0 55 H210 Q222 55 228 42 Q232 36 244 36 H496 V60 H0Z" fill="var(--cream)"/>
  </svg>
  <h2 class="abs cond band discount" style="background:none">£150 Discount on Installations</h2>
  <p class="abs terms">*terms and conditions apply</p>
  <div class="abs phones" role="img" aria-label="Two smartphones showing the security system control app"></div>

  <h2 class="abs provider">NOT HAPPY WITH YOUR<br>CURRENT PROVIDER?</h2>
  <p class="abs survey">Free of charge no obligation <span class="hl">take over survey and quotation</span> <b>and up to £100 off</b></p>
  <p class="abs point" style="left:57px;top:456px;width:230px">CCTV systems starting from £595 + VAT<br>(based on 2 cameras)</p>
  <p class="abs point" style="left:57px;top:497px;width:260px">K M Guard Solutions are always there, always available, wherever and whenever you need us.</p>

  <div class="abs brand">
    <span class="mark"></span>
    <span class="name">K M GUARD<br>SOLUTIONS</span>
  </div>

  <p class="abs contact-label">Contact Us</p>
  <p class="abs cond phone-big">01632 480913</p>
  <p class="abs web">www.kmguardsolutions.co.uk</p>
  <p class="abs email">operations@kmguardsolutions.co.uk</p>
  <p class="abs address">27 Harwood Lane, Brentwood,<br>Essex, CM15-9QX</p>

  <svg class="abs footer" viewBox="0 0 496 19" preserveAspectRatio="none" aria-hidden="true">
    <rect width="496" height="19" fill="var(--black)"/>
    <path d="M220 19 L236 0 H240 L224 19Z" fill="var(--white)"/>
    <path d="M228 19 L244 0 H496 V19Z" fill="var(--orange)"/>
  </svg>
</section>

<section class="flyer flyer--back">
  <div class="abs header">
    <h1 class="abs back-title">Are you looking to keep you<br>and your premises safe?</h1>
  </div>
  <div class="abs photo" style="left:0;top:104px;width:236px;height:195px;background:linear-gradient(135deg,#f2f2f2,#9aa3ad 50%,#5b84c4)" role="img" aria-label="Close-up of a chrome alarm keypad with a blue display"></div>
  <div class="abs photo" style="left:236px;top:104px;width:104px;height:195px;background:linear-gradient(180deg,#f5f5f4,#c8c8c6 60%,#6b6b6b)" role="img" aria-label="Photo of a white spiral staircase"></div>
  <div class="abs photo" style="left:340px;top:104px;width:154px;height:195px;background:linear-gradient(160deg,#fafafa,#dfe3ea 50%,#e7c7b2)" role="img" aria-label="Hand pressing buttons on a white alarm keypad"></div>

  <svg class="abs" style="left:0;top:299px" width="330" height="60" viewBox="0 0 330 60" aria-hidden="true">
    <rect width="330" height="60" fill="var(--black)"/>
    <path d="M0 55 H258 Q268 55 274 42 Q278 36 290 36 H330 V60 H0Z" fill="var(--cream)"/>
  </svg>
  <h2 class="abs cond band view" style="background:none">VIEW, CONTROL AND MANAGE YOUR SECURITY<br>SYSTEMS <span class="o">ANYWHERE IN THE WORLD</span></h2>

  <p class="abs point back-point" style="top:366px">K M Guard Solutions install, maintain and repair all intruder alarms, CCTV, intercom and access control</p>
  <p class="abs point back-point" style="top:414px">Feel at ease with monitoring services &amp; police response tailored to suit you and your business</p>
  <p class="abs point back-point" style="top:463px">K M Guard can takeover any existing security system and offer maintenance checks to guarantee the best performance for you and your premises</p>
  <p class="abs point back-point" style="top:525px">K M Guard understand that being security conscious is ever increasing, protecting your property and family is a number one priority</p>
  <p class="abs point back-point" style="top:574px">Our fully insured and accredited team offer quality, safety and cost efficiency throughout the whole process</p>
  <p class="abs point back-point" style="top:623px">K M Guard Solutions are using the latest cloud-based technology to stay connected with your home and business 24/7</p>

  <div class="abs cta">
    <p>If you are looking to improve the security in your home, office or commercial property then call a member of our team today for a free quote.</p>
    <h3>FULLY INSURED<br>AND ACCREDITED</h3>
  </div>

  <div class="abs listing" role="img" aria-label="Tradevouch membership badge"><span></span></div>
  <div class="abs cert" style="left:318px" role="img" aria-label="NQPB CCTV systems certification badge"><i></i><em></em></div>
  <div class="abs cert" style="left:372px" role="img" aria-label="NQPB intruder alarm systems certification badge"><i></i><em></em></div>
  <div class="abs cert" style="left:426px" role="img" aria-label="Product certification badge"><i style="border-radius:4px"></i><em></em></div>

  <p class="abs cond back-phone">01632 480913</p>
  <p class="abs back-web">www.kmguardsolutions.co.uk</p>

  <svg class="abs footer" viewBox="0 0 494 19" preserveAspectRatio="none" aria-hidden="true">
    <rect width="494" height="19" fill="var(--black)"/>
    <path d="M0 0 H268 L284 19 H0Z" fill="var(--orange)"/>
    <path d="M272 0 H276 L292 19 H288Z" fill="var(--white)"/>
  </svg>
</section>

</body>
</html>
```